Beautify our company's one pager website

We need a website - currently we have only a nice light-switcher: https://brimvale.example

We got the basic contents together (see the wireframes - also in SVG format -
attached here). Now we need you (!) to make it look appealing, create proper illustrations, provide a good theme picture and advice us on how to take good employee pictures.

In the wireframes, the picture and most illustrations are just placeholders (only the logos of "Our Open Source tools" are ours - see attached logos.svg). We request you to fill all placeholders with good illustrations and make the whole page look nicely.

Only one color is pre-defined (#11233f - the blue color we use for our logo when it is on white background). Feel free to give it nice colours based on your professional expertise and intuition. Feel also free to use the blue in a more creative way, than proposed in the wireframes.

We will do the coding ourselves, but we request you to submit a responsive design, with at least one version for mobiles, one for tablet size and one for full desktop resolution.

We think our people pictures should follow a design line. Please asses us on how we should take our colleagues' pictures (e.g. completely white background, or... blurry city background, or.... with a big box in the hand, etc... we are curious to see your suggestion).

In case of any doubts, please don't hesitate to contact us (brimvale-website-design@brimvale.example).

Target Market(s)

International cooperation agencies

Industry/Entity Type

Consulting

Number of Pages Required

3 page

Font styles to use
Other font styles liked:
• Lato

Colors

Designer to choose colors to be used in the design.

Requirements
Must have
• Responsive design in mind (one pager, for three different resolutions: mobile, tablet, desktop)
• Illustrations and (maybe) a photo - must be royalty-free and open for any use in the future.
Nice to have
• SVG formated design
• Suggestions on the peoples' photos

```html
<!DOCTYPE html>
<html lang="en">
<head>
<meta charset="utf-8">
<title>Brimvale – Agile Consultancies</title>
<link href="https://fonts.googleapis.com/css2?family=Poppins:wght@300;400;500;600;700&display=swap" rel="stylesheet">
<style>
:root{
  --navy:#11233f;
  --blue:#1d3d7a;
  --blue-mid:#2456a6;
  --cyan:#1aa3e0;
  --teal:#16a0c8;
  --ink:#222a35;
  --muted:#6b7380;
  --line:#d7dbe2;
  --grey-bg:#f3f4f6;
  --white:#ffffff;
  --dark:#262729;
  --panel:#2e2f31;
}
*{box-sizing:border-box;margin:0;padding:0}
html,body{width:1200px;height:4444px;overflow:hidden}
body{font-family:'Poppins',sans-serif;color:var(--ink);background:var(--white);position:relative}
.abs{position:absolute}
a{color:inherit;text-decoration:none}

/* header */
.site-header{position:absolute;top:0;left:0;width:1200px;height:86px;background:linear-gradient(#fff,#eef0f3);display:flex;align-items:center;padding:0 110px;justify-content:space-between}
.brand{font-weight:700;font-size:26px;color:var(--navy);letter-spacing:1px}
.main-nav{display:flex;gap:42px;font-size:14px;font-weight:500;color:var(--navy)}
.main-nav a{padding:7px 18px;border-radius:16px}
.main-nav a.active{background:var(--navy);color:#fff}

/* hero */
.hero{position:absolute;top:86px;left:0;width:1200px;height:474px;background:radial-gradient(ellipse at 50% 75%,#3fd0e6 0%,#1a8ccf 28%,#134f9c 60%,#0f2d66 100%);color:#fff;text-align:center}
.hero h1{margin-top:48px;font-size:40px;font-weight:600;letter-spacing:1px}
.hero h2{font-size:26px;font-weight:500;margin-top:-4px}
.hero p{width:1000px;margin:18px auto 0;font-size:12.5px;line-height:22px;opacity:.95}
.hero-visual{position:absolute;left:390px;top:200px;width:420px;height:300px;border-radius:14px 14px 4px 4px;background:linear-gradient(#e9eef3,#b9c6d2);box-shadow:0 10px 20px rgba(0,0,0,.25)}

/* about */
.about-deco{position:absolute;left:0;top:590px;width:360px;height:360px}
.about-photo{position:absolute;left:115px;top:655px;width:295px;height:235px;border:6px solid var(--blue);background:linear-gradient(135deg,#cfd8e2,#8fa4bd 60%,#c9a87d)}
.about h2{position:absolute;left:490px;top:648px;font-size:40px;font-weight:600;color:var(--navy)}
.about p{position:absolute;left:490px;top:712px;width:600px;font-size:12.5px;line-height:21px;color:var(--muted)}
.btn-outline{position:absolute;left:490px;top:842px;width:96px;height:36px;border:1.5px solid var(--navy);border-radius:18px;font-size:11px;font-weight:600;color:var(--navy);display:flex;align-items:center;justify-content:center}

/* agile */
.agile{position:absolute;top:955px;left:0;width:1200px;height:215px;background:linear-gradient(120deg,#142f63,#1e4a94 55%,#173b78);color:#fff;text-align:center}
.agile h2{margin-top:42px;font-size:40px;font-weight:400}
.agile p{width:880px;margin:14px auto 0;font-size:13px;line-height:24px}

/* services */
.services-head{position:absolute;top:1225px;width:1200px;text-align:center}
.services-head h2{font-size:40px;font-weight:600;color:var(--navy)}
.services-head p{font-size:12px;color:var(--muted)}
.timeline{position:absolute;left:599px;top:1360px;width:2px;height:860px;background:var(--line)}
.dot{position:absolute;width:12px;height:12px;border-radius:50%;background:var(--navy)}
.service h3{font-size:21px;font-weight:500;color:var(--navy);margin-bottom:8px}
.service p{font-size:12.5px;line-height:20px;color:var(--muted)}
.tablet{position:absolute;border:2px solid #dfe2e6;border-radius:18px;background:#fafbfc;box-shadow:0 2px 6px rgba(0,0,0,.06)}
.tablet .screen{position:absolute;left:30px;top:14px;right:30px;bottom:14px;background:#fff;border:1px solid #eceef1;display:flex;align-items:center;justify-content:center}
.tablet .screen div{width:130px;height:120px;border-radius:50%;background:radial-gradient(#c9dca3,#9fbf5f)}
.btn-solid{position:absolute;left:522px;top:2265px;width:156px;height:38px;border-radius:19px;background:var(--navy);color:#fff;font-size:11px;font-weight:600;display:flex;align-items:center;justify-content:center}

/* tools */
.tools{position:absolute;top:2375px;left:0;width:1200px;height:430px;background:linear-gradient(120deg,#0f2a5e,#1f4f9c 50%,#0f2a5e);}
.tools h2{position:absolute;top:68px;width:1200px;text-align:center;color:#fff;font-size:40px;font-weight:600}
.tool-card{position:absolute;top:160px;width:485px;height:255px;text-align:center;padding:30px 40px 0}
.tool-card.k1{left:115px;background:var(--cyan);color:#fff}
.tool-card.k2{left:600px;background:#fff;color:var(--ink);box-shadow:0 6px 14px rgba(0,0,0,.15)}
.tool-card .name{font-size:18px;margin:10px 0 12px}
.tool-card p{font-size:12px;line-height:19px}
.tool-card .link{font-size:12.5px;margin-top:14px;text-decoration:underline}

/* team */
.team{position:absolute;top:2805px;left:0;width:1200px;height:1155px;background:var(--grey-bg)}
.team h2{position:absolute;top:78px;width:1200px;text-align:center;font-size:40px;font-weight:600;color:var(--navy)}
.team .sub{position:absolute;top:132px;width:1200px;text-align:center;font-size:13px;color:var(--muted)}
.member{position:absolute;width:290px;text-align:center}
.member .photo{width:196px;height:196px;border-radius:50%;margin:0 auto 22px}
.member .name{font-size:16px;font-weight:500;color:var(--navy)}
.member .role{font-size:12px;color:var(--muted)}
.member.featured{background:#fff;box-shadow:0 4px 14px rgba(0,0,0,.15);padding:22px 0 30px}
.ph-a{background:linear-gradient(160deg,#c9cfb7,#8a6c55 60%,#4d5559)}
.ph-b{background:linear-gradient(160deg,#d9d2c4,#c69b5e 55%,#7e8da0)}
.ph-c{background:linear-gradient(160deg,#c5cbd1,#b5895f 55%,#3c3f47)}

/* contact */
.contact{position:absolute;top:3960px;left:0;width:1200px;height:350px;background:var(--dark)}
.map{position:absolute;left:635px;top:0;width:565px;height:350px;background:linear-gradient(135deg,#eceae4,#dcdcd6)}
.contact-info{position:absolute;left:190px;top:60px;color:#fff;font-size:12.5px;line-height:20px}
.contact-info .brand{color:#fff;font-size:26px;margin-bottom:22px}
.info-row{display:flex;gap:16px;align-items:flex-start;margin-bottom:12px}
.info-row svg{flex:none;margin-top:3px}
.contact-form{position:absolute;left:520px;top:25px;width:285px;height:305px;background:var(--panel);padding:16px 20px;color:#fff}
.contact-form h3{font-size:20px;font-weight:500;margin-bottom:14px}
.field{background:#fff;height:34px;margin-bottom:12px;font-size:11px;color:#999;padding:9px 10px}
.field.msg{height:56px}
.send{width:70px;height:30px;background:var(--blue);font-size:10px;font-weight:600;display:flex;align-items:center;justify-content:center}

/* footer */
.site-footer{position:absolute;top:4310px;left:0;width:1200px;height:134px;background:var(--navy);color:#fff;text-align:center}
.foot-nav{display:flex;justify-content:center;gap:80px;font-size:11.5px;margin-top:30px}
.social{display:flex;justify-content:center;gap:20px;margin-top:16px}
.social span{width:16px;height:16px;border-radius:50%;background:#fff}
.copy{font-size:10.5px;margin-top:12px;opacity:.9}
</style>
</head>
<body>

<header class="site-header">
  <div class="brand">BRIMVALE</div>
  <nav class="main-nav">
    <a class="active">HOME</a><a>ABOUT</a><a>SERVICES</a><a>TOOLS</a><a>TEAM</a><a>CONTACT</a>
  </nav>
</header>

<section class="hero">
  <h1>AGILE CONSULTANCIES</h1>
  <h2>For International Development</h2>
  <p><strong>Brimvale</strong> provides institutions working in the international cooperation field (implementing agencies, local governmental and non-governmental institutions) with solutions (hardware, software and consultancy services) to better organise, manage and exchange their knowledge.</p>
  <div class="hero-visual" role="img" aria-label="Illustration of a laptop showing a glowing light bulb surrounded by service icons"></div>
</section>

<section class="about">
  <svg class="about-deco" viewBox="0 0 360 360" aria-hidden="true">
    <rect x="0" y="25" width="140" height="300" rx="60" fill="#e4e6ea"/>
    <rect x="-60" y="90" width="220" height="60" rx="30" fill="#eceef1"/>
  </svg>
  <div class="about-photo" role="img" aria-label="Photo of a smiling student holding books in a corridor"></div>
  <h2>ABOUT US</h2>
  <p>We help partners in international cooperation turn scattered know-how into shared, usable knowledge. Our small team blends field experience with modern technology, building open tools and clear processes so that agencies, ministries and local groups can learn faster, decide better and work together across borders. We listen first, test early, and improve step by step with the people who will use the result every day, keeping every solution simple, open and sustainable.</p>
  <a class="btn-outline">READ MORE</a>
</section>

<section class="agile">
  <h2>Agile</h2>
  <p>Efficient and flexible methodology for developing successful solutions with fun. Is is based on iterative, measurable and verifiable small steps, with integrative and empowering involvement of all actors.</p>
</section>

<section class="services">
  <div class="services-head">
    <h2>SERVICES</h2>
    <p>Practical support for knowledge, technology and organisations in international cooperation</p>
  </div>
  <div class="timeline"></div>
  <div class="dot" style="left:594px;top:1466px"></div>
  <div class="dot" style="left:594px;top:1771px"></div>
  <div class="dot" style="left:594px;top:2079px"></div>

  <div class="service abs" style="left:185px;top:1410px;width:380px">
    <h3>Technology For International Aid</h3>
    <p>Meaningful implementation and application of Digital Media, Software and Hardware with a sensibility for the world.</p>
  </div>
  <div class="tablet" style="left:655px;top:1360px;width:345px;height:172px"><div class="screen"><div role="img" aria-label="Illustration of a light bulb"></div></div></div>

  <div class="tablet" style="left:180px;top:1695px;width:345px;height:168px"><div class="screen"><div role="img" aria-label="Illustration of hands holding a leaf"></div></div></div>
  <div class="service abs" style="left:660px;top:1716px;width:370px">
    <h3>Organizational Development</h3>
    <p>Agile and data-driven approach to accompany organizations into change processes: approach to accompany organizations.</p>
  </div>

  <div class="service abs" style="left:185px;top:2022px;width:380px">
    <h3>Data and Knowledge Management</h3>
    <p>Needs assessment, organizational and requirement analysis for ICT-based support to knowledge processes in communities of practice.</p>
  </div>
  <div class="tablet" style="left:665px;top:1955px;width:340px;height:245px"><div class="screen"><div role="img" aria-label="Illustration of recycling arrows"></div></div></div>

  <a class="btn-solid">GET STARTED NOW</a>
</section>

<section class="tools">
  <h2>OUR OPEN SOURCE TOOLS</h2>
  <div class="tool-card k1">
    <svg width="60" height="50" viewBox="0 0 60 50" aria-hidden="true"><rect x="12" y="10" width="36" height="30" rx="4" fill="none" stroke="#fff" stroke-width="2.5"/></svg>
    <div class="name">D-VAULT</div>
    <p>Open Source web-based document management system. This software allows organisational groups to flexibly manage their knowledge through documents and data. The files can be structured and access can be managed for groups of people or for specific persons.</p>
    <div class="link">https://code.brimvale.example/d-vault</div>
  </div>
  <div class="tool-card k2">
    <svg width="60" height="50" viewBox="0 0 60 50" aria-hidden="true"><rect x="14" y="8" width="32" height="34" fill="none" stroke="#333" stroke-width="2.5"/></svg>
    <div class="name">D-BRIDGE</div>
    <p>Several decentralized D-Vaults can be connected over a D-Bridge. This allows to manage between different instances and create organizational partnerships for networks of providing access to information and enhance knowledge in the developing world.</p>
    <div class="link">https://code.brimvale.example/d-bridge</div>
  </div>
</section>

<section class="team">
  <h2>OUR TEAM</h2>
  <div class="sub">We are cultural technologists</div>

  <div class="member" style="left:115px;top:202px"><div class="photo ph-a" role="img" aria-label="Portrait photo of a team member"></div><div class="name">Dr. Marco Fenwick</div><div class="role">Chief Executive Officer</div></div>
  <div class="member" style="left:455px;top:202px"><div class="photo ph-b" role="img" aria-label="Portrait photo of a team member"></div><div class="name">Irena Valdis</div><div class="role">Chief Operations Officer</div></div>
  <div class="member" style="left:795px;top:202px"><div class="photo ph-c" role="img" aria-label="Portrait photo of a team member"></div><div class="name">Tomas Hallberg</div><div class="role">Digital Product manager</div></div>

  <div class="member" style="left:115px;top:512px"><div class="photo ph-a" role="img" aria-label="Portrait photo of a team member"></div><div class="name">Dr. Marco Fenwick</div><div class="role">Chief Executive Officer</div></div>
  <div class="member featured" style="left:455px;top:500px"><div class="photo ph-b" role="img" aria-label="Portrait photo of a team member"></div><div class="name">Irena Valdis</div><div class="role">Chief Operations Officer</div></div>
  <div class="member" style="left:795px;top:512px"><div class="photo ph-c" role="img" aria-label="Portrait photo of a team member"></div><div class="name">Tomas Hallberg</div><div class="role">Digital Product manager</div></div>

  <div class="member" style="left:115px;top:838px"><div class="photo ph-a" role="img" aria-label="Portrait photo of a team member"></div><div class="name">Dr. Marco Fenwick</div><div class="role">Chief Executive Officer</div></div>
  <div class="member" style="left:455px;top:838px"><div class="photo ph-b" role="img" aria-label="Portrait photo of a team member"></div><div class="name">Irena Valdis</div><div class="role">Chief Operations Officer</div></div>
  <div class="member" style="left:795px;top:838px"><div class="photo ph-c" role="img" aria-label="Portrait photo of a team member"></div><div class="name">Tomas Hallberg</div><div class="role">Digital Product manager</div></div>
</section>

<section class="contact">
  <div class="map" role="img" aria-label="Street map showing the office location"></div>
  <div class="contact-info">
    <div class="brand">BRIMVALE</div>
    <div class="info-row"><svg width="16" height="16" viewBox="0 0 24 24"><path d="M6.6 10.8a15 15 0 0 0 6.6 6.6l2.2-2.2c.3-.3.7-.4 1-.2 1.1.4 2.3.6 3.6.6.6 0 1 .4 1 1V20c0 .6-.4 1-1 1A17 17 0 0 1 3 4c0-.6.4-1 1-1h3.5c.6 0 1 .4 1 1 0 1.3.2 2.5.6 3.6.1.3 0 .7-.2 1z" fill="#fff"/></svg><span style="font-size:15px">+(00) 555 010 203</span></div>
    <div class="info-row"><svg width="16" height="14" viewBox="0 0 24 20"><rect x="1" y="2" width="22" height="16" rx="2" fill="none" stroke="#fff" stroke-width="2"/><path d="M2 4l10 7 10-7" fill="none" stroke="#fff" stroke-width="2"/></svg><span>hello@brimvale.example</span></div>
    <div class="info-row"><svg width="16" height="20" viewBox="0 0 24 30"><path d="M12 0a10 10 0 0 0-10 10c0 8 10 20 10 20s10-12 10-20A10 10 0 0 0 12 0zm0 14a4 4 0 1 1 0-8 4 4 0 0 1 0 8z" fill="#fff"/></svg><span>Brimvale Ltd<br>Larkspur Lane 14, 00000 Northam,<br>Freeland</span></div>
    <div style="margin-left:32px">To be defined street Eastport, Freeland</div>
    <div style="margin-left:32px;text-decoration:underline">Impressum</div>
  </div>
  <form class="contact-form">
    <h3>CONTACT US</h3>
    <div class="field">Name</div>
    <div class="field">Email</div>
    <div class="field msg">Message</div>
    <div class="send">SEND</div>
  </form>
</section>

<footer class="site-footer">
  <nav class="foot-nav"><a>ABOUT</a><a>SERVICES</a><a>TOOLS</a><a>TEAM</a><a>CONTACT</a></nav>
  <div class="social"><span></span><span></span><span></span><span></span></div>
  <div class="copy">Copyright 2017 © All Rights Reserved</div>
</footer>

</body>
</html>
```